Quiet Otter non alcohol beer can design

We are after 3 label designs for a new non alcoholic beer company (Quiet Otter). The colours to be used would primarily be a soft pink, blue, and white. Each label would essentially call out one dominant colour and the other two incorporated. Base of the design fun and eye-catching but still a modern clean aesthetic. A guide would be a general tie-dye colour all over the can with bold writing of the style of beer in one of the contrasting colours. Our logo then featuring in one of the secondary colours.
Eg: combined pink, blue and white can with white being dominant pink beer style and blue logo. Colours alternated on other varieties.
The varieties of beer are (HAZY) (RADLER) and (IPA)
Updates
Hi all, thank-you for the many and varied designs. Some have really hit the brief. We will review all tomorrow and get back to you ASAP. Thanks again for the great work and effort.
Target Market(s)
outdoorsy/active/health conscious
Industry/Entity Type
Beverage
Look and feel
Each slider illustrates characteristics of the customer's brand and the style your logo design should communicate.

```html
<!DOCTYPE html>
<html lang="en">
<head>
<meta charset="utf-8">
<title>Quiet Otter – Hazy can label</title>
<link rel="stylesheet" href="https://fonts.googleapis.com/css2?family=Montserrat:wght@600;700&display=swap">
<style>
  :root {
    --backdrop: #e9eaea;
    --can-blue: #2056a0;
    --can-pink: #f2dbe4;
    --can-white: #f8f8f8;
    --style-yellow: #f5d933;
    --brand-ink: #1f4f94;
  }
  * { box-sizing: border-box; margin: 0; padding: 0; }
  html, body {
    width: 1032px;
    height: 1200px;
    overflow: hidden;
    background: var(--backdrop);
  }
  .canvas {
    position: relative;
    width: 1032px;
    height: 1200px;
  }
  .label-panel {
    position: absolute;
    top: 75px;
    width: 428px;
    height: 1053px;
    overflow: hidden;
  }
  .label-panel--back { left: 57px; }
  .label-panel--front { left: 564px; }
  .label-pattern {
    position: absolute;
    inset: 0;
  }
  .label-panel--back .label-pattern {
    background: linear-gradient(160deg,
      var(--can-blue) 0%, var(--can-white) 22%, var(--can-blue) 40%,
      var(--can-pink) 55%, var(--can-blue) 72%, var(--can-white) 85%, var(--can-blue) 100%);
  }
  .label-panel--front .label-pattern {
    background: linear-gradient(180deg,
      var(--can-blue) 0%, var(--can-white) 26%, var(--can-white) 48%,
      var(--can-blue) 70%, var(--can-pink) 86%, var(--can-pink) 100%);
  }
  .beer-style {
    position: absolute;
    top: 366px;
    left: 84px;
    font-family: "Montserrat", sans-serif;
    font-weight: 700;
    font-size: 78px;
    line-height: 1;
    letter-spacing: 0.2em;
    color: var(--style-yellow);
  }
  .brand-mark {
    position: absolute;
    top: 900px;
    left: 0;
    width: 100%;
    display: flex;
    align-items: center;
    justify-content: center;
    gap: 12px;
  }
  .brand-dot {
    width: 22px;
    height: 22px;
    border-radius: 50%;
    background: var(--brand-ink);
  }
  .brand-name {
    font-family: "Montserrat", sans-serif;
    font-weight: 700;
    font-size: 34px;
    color: var(--brand-ink);
  }
</style>
</head>
<body>
  <main class="canvas">
    <section class="label-panel label-panel--back">
      <div class="label-pattern" role="img" aria-label="Bold blue blob pattern over white with soft pink patches, wrapping the can"></div>
    </section>

    <section class="label-panel label-panel--front">
      <div class="label-pattern" role="img" aria-label="Bold blue blob pattern over white with soft pink patches, wrapping the can"></div>
      <h1 class="beer-style">HAZY</h1>
      <div class="brand-mark">
        <span class="brand-dot"></span>
        <span class="brand-name">Quiet Otter</span>
      </div>
    </section>
  </main>
</body>
</html>
```